Corvelle Strategies business card

I need a business card for my new strategic consulting LLC, Corvelle Strategies. We specialize in helping people who care about broadband technology and telecommunications policy, and we're based in Washington DC. I'm looking for a card that says smart, credible, future-facing and signals a high level of expertise. It's DC, so there's clearly a limit to how crazy we can go with this card, but I am looking for a design that reflects a company that is comfortable with technology, policy, and having a little bit fun. I'm uploading my logo below, and I'd like to have it be part of the card design in some fashion.
Target Market(s)
Telecommunications and technology policy professionals
Industry/Entity Type
Technology policy
Contact Information for Business Card
Name of business, my name (Glen Mosswater), email (glen@corvellestrategies-example.com) , phone number (202-555-0148)phone number

```html
<!DOCTYPE html>
<html lang="en">
<head>
<meta charset="utf-8">
<title>Corvelle Strategies — Business Card</title>
<link href="https://fonts.googleapis.com/css2?family=Montserrat:wght@500;600;700&family=Inter:wght@400;500&display=swap" rel="stylesheet">
<style>
  :root {
    --canvas: #e9e9eb;
    --card: #fbfbfb;
    --navy: #0f3f91;
    --navy-deep: #00234f;
    --ink: #1c2d55;
    --gold: #f8b04b;
    --white: #ffffff;
    --muted: #c9d2e3;
  }
  * { box-sizing: border-box; margin: 0; padding: 0; }
  html, body { width: 968px; height: 1200px; overflow: hidden; }
  body { background: var(--canvas); position: relative; font-family: "Montserrat", sans-serif; }

  .card {
    position: absolute;
    width: 699px; height: 389px;
    background: var(--card);
    border-radius: 24px;
    overflow: hidden;
    box-shadow: 0 18px 30px rgba(0,0,0,0.18);
  }
  .card--front { left: 132px; top: 170px; }
  .card--back  { left: 133px; top: 638px; }

  /* Front */
  .brand {
    position: absolute; display: flex; align-items: center; gap: 10px;
    font-family: "Montserrat", sans-serif; font-weight: 700;
    white-space: nowrap;
  }
  .brand__dot { border-radius: 50%; background: var(--gold); flex: none; }
  .card--front .brand { left: 56px; top: 152px; font-size: 28px; color: var(--navy); }
  .card--front .brand__dot { width: 22px; height: 22px; }

  .rule { position: absolute; left: 59px; top: 227px; width: 43px; height: 2px; background: var(--gold); }
  .tagline {
    position: absolute; left: 59px; top: 240px;
    font-size: 10.5px; font-weight: 500; letter-spacing: 2.6px; line-height: 15px;
    color: var(--ink);
  }
  .hero { position: absolute; left: 0; top: 0; }

  /* Back */
  .band { position: absolute; left: 0; top: 84px; width: 699px; height: 221px; background: var(--navy-deep); }
  .person { position: absolute; left: 57px; top: 138px; color: var(--white); }
  .person__name { font-size: 21px; font-weight: 700; letter-spacing: 0.2px; }
  .person__role { margin-top: 4px; font-size: 10.5px; font-weight: 600; letter-spacing: 2.6px; color: var(--gold); }
  .contact {
    position: absolute; left: 58px; display: flex; align-items: center; gap: 12px;
    font-family: "Inter", sans-serif; font-size: 12px; color: var(--white);
    white-space: nowrap;
  }
  .contact--email { top: 201px; }
  .contact--phone { top: 227px; letter-spacing: 0.6px; }
  .contact svg { width: 18px; height: 14px; flex: none; }
  .divider { position: absolute; left: 328px; top: 134px; width: 1px; height: 116px; background: rgba(255,255,255,0.35); }
  .card--back .brand { left: 382px; top: 160px; font-size: 24px; color: var(--white); }
  .card--back .brand__dot { width: 18px; height: 18px; }
  .services {
    position: absolute; left: 366px; top: 234px;
    font-family: "Inter", sans-serif; font-size: 8.5px; font-weight: 500; letter-spacing: 0.7px;
    color: var(--muted); white-space: nowrap;
  }
  .services .sep { color: var(--gold); margin: 0 8px; }
</style>
</head>
<body>

<section class="card card--front">
  <svg class="hero" width="699" height="389" viewBox="0 0 699 389">
    <defs>
      <linearGradient id="cityGlow" x1="0" y1="0" x2="1" y2="1">
        <stop offset="0" stop-color="#1f5fb4"/>
        <stop offset="0.55" stop-color="#174a93"/>
        <stop offset="1" stop-color="#0c2d68"/>
      </linearGradient>
    </defs>
    <polygon points="521,76 699,76 699,302 410,302" fill="url(#cityGlow)" role="img" aria-label="Photo of the Capitol dome at night with glowing network lines"/>
    <polygon points="410,302 699,302 699,319 401,319" fill="var(--gold)"/>
  </svg>
  <div class="brand"><span>Corvelle Strategies</span><span class="brand__dot"></span></div>
  <div class="rule"></div>
  <p class="tagline">STRATEGIC INSIGHT.<br>CONNECTED FUTURES.</p>
</section>

<section class="card card--back">
  <div class="band"></div>
  <svg class="hero" width="699" height="389" viewBox="0 0 699 389">
    <polygon points="392,296 699,296 699,313 382,313" fill="var(--gold)"/>
  </svg>
  <div class="person">
    <p class="person__name">Glen Mosswater</p>
    <p class="person__role">FOUNDER &amp; PRINCIPAL</p>
  </div>
  <div class="contact contact--email">
    <svg viewBox="0 0 18 14" fill="none" stroke="var(--gold)" stroke-width="1.2"><rect x="0.6" y="0.6" width="16.8" height="12.8"/><path d="M0.6 0.6 L9 8 L17.4 0.6 M0.6 13.4 L6.5 6 M17.4 13.4 L11.5 6"/></svg>
    <span>glen@corvellestrategies-example.com</span>
  </div>
  <div class="contact contact--phone">
    <svg viewBox="0 0 18 14"><path d="M3 1 L5.5 0.5 L7 4 L5.5 5.3 C6.3 7.3 7.7 8.7 9.7 9.5 L11 8 L14.5 9.5 L14 12 C13.5 13 12.5 13.5 11 13.2 C6.5 12 3 8.5 2 4 C1.7 2.5 2 1.5 3 1 Z" fill="var(--gold)"/></svg>
    <span>202-555-0148</span>
  </div>
  <div class="divider"></div>
  <div class="brand"><span>Corvelle Strategies</span><span class="brand__dot"></span></div>
  <p class="services">BROADBAND<span class="sep">|</span>TELECOM POLICY<span class="sep">|</span>STRATEGIC ADVOCACY</p>
</section>

</body>
</html>
```